Tri-fold Brochure Design - Roll Fold

I am seeking a designer to create tri-fold brochure for my business, which sells color caulk. While I have created a very rough draft of 4 pages (attached), these should not be considered final and should be updated with a new layout, fonts, and images as needed. Also, The purple/lilac background color of these 4 pages does not align with my brand and should be changed.

The design should be inspired by my website, logo, or business cards, with a focus on the flowing shapes featured on the business cards. The brochure's ultimate goal is to entice potential customers to visit my website at www.brightbeadsealant.com. brochure will be roll folded.

Looking forward to seeing what you have. Thank you!

Target Market(s)

Construction, architects, designers, and painters.

Requirements
Must have
• 2 pages of new content, new layout & design, new color scheme.

```html
<!DOCTYPE html>
<html lang="en">
<head>
<meta charset="UTF-8">
<title>Bright Bead Sealant – Tri-fold Brochure</title>
<link href="https://fonts.googleapis.com/css2?family=Montserrat:wght@400;500;600;700;800&display=swap" rel="stylesheet">
<style>
  :root {
    --bg: #d6d6d6;
    --paper: #efecec;
    --paper-shade: #e3e0e0;
    --navy: #2a2846;
    --text: #3b3a45;
    --orange: #ec5f2a;
    --orange-deep: #d23c14;
    --orange-band: #e63a10;
    --green: #2f9a6a;
    --red: #e02a2a;
  }
  * { box-sizing: border-box; margin: 0; padding: 0; }
  html, body { width: 1200px; height: 900px; overflow: hidden; }
  body {
    background: var(--bg);
    font-family: "Montserrat", sans-serif;
    position: relative;
  }
  .brochure {
    position: absolute;
    left: 90px; top: 65px;
    width: 1020px; height: 770px;
    display: flex;
  }
  .panel {
    position: relative;
    width: 340px; height: 770px;
    background: var(--paper);
    overflow: hidden;
  }
  .panel--middle { background: linear-gradient(180deg, var(--paper-shade), #dcd8d8); }
  .panel-art {
    position: absolute; inset: 0;
    width: 100%; height: 100%;
  }
  .panel-content {
    position: relative;
    padding: 26px 26px 0;
    text-align: center;
    color: var(--text);
  }
  .heading {
    color: var(--navy);
    font-weight: 700;
    font-size: 25px;
    line-height: 1.2;
  }
  .body-copy {
    font-size: 12.5px;
    line-height: 1.6;
    margin-top: 12px;
  }
  .body-copy + .body-copy { margin-top: 9px; }
  .body-copy strong { font-weight: 700; }
  .photo {
    width: 212px; height: 190px;
    margin: 18px auto 0;
    border: 2px solid var(--orange);
    border-radius: 34px 0 34px 0;
    background: linear-gradient(135deg, #6f7a7c, #c9cfcf 45%, #e25a3a 60%, #3a3a3a);
  }
  .heading--small { font-size: 21px; margin-top: 27px; }
  .lead {
    color: var(--green);
    font-size: 13px;
    line-height: 1.55;
    margin-top: 14px;
  }
  .lead strong { font-weight: 700; }
  .tagline {
    color: var(--red);
    font-weight: 600;
    font-size: 18px;
    margin-top: 24px;
  }
  .website {
    color: var(--navy);
    font-size: 16px;
    margin-top: 4px;
  }
  .website strong { font-weight: 700; }
  .brand {
    position: absolute;
    left: 0; right: 0; top: 355px;
    text-align: center;
    color: var(--navy);
    font-weight: 800;
    font-size: 22px;
    line-height: 1.1;
    letter-spacing: 1px;
    text-transform: uppercase;
  }
</style>
</head>
<body>
  <div class="brochure">
    <section class="panel panel--left">
      <svg class="panel-art" viewBox="0 0 340 770" preserveAspectRatio="none" aria-hidden="true">
        <path d="M0 690 C110 660 230 700 340 680 L340 770 L0 770 Z" fill="var(--orange)"/>
        <rect x="0" y="735" width="340" height="35" fill="var(--orange-band)"/>
      </svg>
      <div class="panel-content">
        <h2 class="heading">Bulk Order Ready</h2>
        <p class="body-copy"><strong>Our one-</strong>of-akind caulk mixer was built in house to ensure speed, quality and a perfect match every time.</p>
        <p class="body-copy"><strong>Whether</strong> you're ordering 3 tubes or 300, your order will be there when you need it.</p>
        <div class="photo" role="img" aria-label="Photo of hands holding a caulk gun with a white tube"></div>
        <h2 class="heading heading--small">Next Day Delivery</h2>
        <p class="lead"><strong>Speed</strong> is Key&nbsp; We Match, Mix, And Ship Your Color in a Single Business Day.</p>
        <p class="tagline">Right Color, Right Now</p>
        <p class="website">www.<strong>brightbeadsealant</strong>.com</p>
      </div>
    </section>

    <section class="panel panel--middle">
      <svg class="panel-art" viewBox="0 0 340 770" preserveAspectRatio="none" aria-hidden="true">
        <path d="M0 0 L340 0 L340 60 C240 85 110 50 0 70 Z" fill="var(--orange-deep)"/>
        <path d="M0 725 C110 705 230 740 340 715 L340 770 L0 770 Z" fill="var(--orange-deep)"/>
      </svg>
      <p class="brand">Bright Bead<br>Sealant</p>
    </section>

    <section class="panel panel--right">
      <svg class="panel-art" viewBox="0 0 340 770" preserveAspectRatio="none" aria-hidden="true">
        <path d="M0 0 L340 0 L340 70 C230 50 110 85 0 60 Z" fill="var(--orange)"/>
        <path d="M0 770 L340 770 L340 735 C230 755 110 725 0 745 Z" fill="var(--orange)"/>
      </svg>
      <p class="brand">Bright Bead<br>Sealant</p>
    </section>
  </div>
</body>
</html>
```